Pediatric Vision Care: Myopia Control Brochure

We are a pediatric eye care practice (ophthalmology and optometry). One of our services we offer for children is myopia control, which are strategies for slowing or stopping the progression of nearsightedness. This is a service we need to sell to parents because most insurance won't pay for it. There are different options we offer that can work well for kids in different situations: glasses with Corvane lenses, atropine eye drops, and/or special contact lenses. We need a brochure we can distribute to parents to let them know about this service that would encourage them to buy it for children who need it. Attached is our initial draft brochure created by our staff that provides text that we want to keep. The images and layout can change. We probably need at least one or two photos of kids on the brochure, because this is only something that works for children who are still growing, and the target audience is parents of 4-8 year old children.

Target Market(s)

Parents of 4-8 year old children

Font styles to use
Sans Serif

Requirements
Must have
• I'm uploading our company logo that should be included somewhere on the brochure. You can include contact information (web address, phone number) for our practice that is found on our website: http://www.brookhollowkidsvision.com/
Should not have
• This should not look childish. We need the impression to be friendly but professional, medical, expert.

```html
<!DOCTYPE html>
<html lang="en">
<head>
<meta charset="utf-8">
<title>Brookhollow Kids Vision – Myopia Control Brochure</title>
<link rel="stylesheet" href="https://fonts.googleapis.com/css2?family=Nunito:wght@800;900&family=Mulish:wght@400;600;700&display=swap">
<style>
  :root {
    --canvas: #4a4a4c;
    --green: #8dc63f;
    --green-light: #c9de7a;
    --yellow: #f9cf12;
    --yellow-light: #f7d24a;
    --orange: #e87722;
    --blue: #6673b8;
    --tint-green: #f1f5e3;
    --tint-yellow: #fbf3d0;
    --tint-blue: #f2f3f8;
    --ink: #1d1d1d;
    --white: #ffffff;
  }
  * { box-sizing: border-box; margin: 0; padding: 0; }
  html, body { width: 853px; height: 1200px; overflow: hidden; }
  body {
    background: var(--canvas);
    font-family: "Mulish", Arial, sans-serif;
    color: var(--ink);
    position: relative;
  }
  .sheet {
    position: absolute;
    left: 73px;
    width: 706px;
    height: 498px;
    display: flex;
    overflow: hidden;
  }
  .sheet--outside { top: 75px; }
  .sheet--inside { top: 629px; left: 75px; }
  .panel {
    position: relative;
    width: 235.33px;
    height: 100%;
    overflow: hidden;
  }
  .panel--env { background: var(--tint-green); border-top: 3px solid var(--green); }
  .panel--contact { background: var(--tint-yellow); border-top: 3px solid var(--orange); }
  .panel--cover { background: var(--tint-blue); border-top: 3px solid var(--blue); }
  .panel--lenses { background: var(--green); }
  .panel--drops { background: var(--yellow); }
  .panel--contacts { background: var(--orange); color: var(--white); }

  .heading {
    font-family: "Nunito", Arial, sans-serif;
    font-weight: 900;
    font-size: 16.5px;
    line-height: 1.1;
    letter-spacing: 0.2px;
    position: absolute;
    left: 19px;
    top: 26px;
  }
  .panel--env .heading { color: var(--green); }
  .panel--contact .heading { color: var(--orange); }
  .panel--cover .heading { color: var(--blue); left: 23px; top: 108px; }
  .panel--contacts .heading { color: var(--white); }

  .copy {
    position: absolute;
    left: 19px;
    right: 19px;
    font-size: 9.2px;
    line-height: 1.48;
    text-align: justify;
  }
  .copy p + p { margin-top: 10px; }
  .panel--env .copy { top: 79px; }
  .panel--cover .copy { top: 134px; left: 23px; right: 17px; line-height: 1.34; }
  .panel--cover .copy p + p { margin-top: 6px; }
  .sheet--inside .copy { top: 196px; left: 20px; right: 22px; line-height: 1.34; }

  .photo { position: absolute; }
  .photo--rounded { border-radius: 10px; }

  .map {
    left: 18px; top: 58px; width: 196px; height: 147px;
    border-radius: 10px;
    background: linear-gradient(135deg, #cfe6d6 0%, #e9efe8 45%, #dde7ef 100%);
  }
  .exam-a { left: 18px; top: 218px; width: 95px; height: 121px; border-radius: 8px;
    background: linear-gradient(135deg, #c9d3da, #eef1f3 55%, #b8c4cc); }
  .exam-b { left: 121px; top: 218px; width: 95px; height: 121px; border-radius: 8px;
    background: linear-gradient(135deg, #a7855f, #e6ddd4 50%, #6c8aa8); }

  .practice-name {
    position: absolute; left: 23px; top: 359px;
    font-family: "Nunito", Arial, sans-serif; font-weight: 800;
    font-size: 12.5px; color: var(--orange);
  }
  .address {
    position: absolute; left: 24px; top: 382px; width: 190px;
    font-size: 9.6px; line-height: 1.55;
  }
  .contact-list { position: absolute; left: 21px; top: 424px; list-style: none; }
  .contact-list li {
    display: flex; align-items: center; gap: 8px;
    font-size: 9.4px; height: 19px;
  }
  .contact-list svg { width: 11px; height: 11px; fill: var(--orange); }
  .contact-list strong { color: var(--orange); font-weight: 700; }

  .brand {
    position: absolute; left: 0; right: 0; top: 28px;
    display: flex; align-items: center; justify-content: center; gap: 8px;
  }
  .brand-dot { width: 14px; height: 14px; border-radius: 50%; background: var(--blue); }
  .brand-name {
    font-family: "Mulish", Arial, sans-serif; font-weight: 700;
    font-size: 15px; line-height: 1.15; color: var(--ink);
  }

  .media-box {
    left: 20px; top: 68px; width: 190px; height: 106px;
    border-radius: 9px;
  }
  .media-box--glasses { background: linear-gradient(135deg, #b9a48c, #e7e1d8 50%, #8ea27a); }
  .media-box--drops { background: linear-gradient(135deg, #b5bcc6, #eef0f3 55%, #c2c8d0); }
  .media-box--lens { background: linear-gradient(160deg, #e4e8ee, #ffffff 60%, #dfe4ea); }

  .footer-art {
    position: absolute; left: 0; bottom: 0; width: 100%;
  }
</style>
</head>
<body>

<section class="sheet sheet--outside">

  <article class="panel panel--env">
    <h2 class="heading">ENVIRONMENTAL<br>OPTIONS</h2>
    <div class="copy">
      <p>All myopic children can benefit from these lifestyle changes. It is important to get your child outdoors consistently. There is strong evidence that children who spend at least 2 hours a day outdoors are less likely to become myopic, and their myopia progresses slower than children who are outdoors less. Some studies show that increasing outdoor time by as few as 45 minutes a day is beneficial in reducing progression.</p>
      <p>There is some evidence that consistent use of screens, particularly held very close to the face, can worsen nearsightedness. We recommend limiting nonacademic screen time and near work, and encourage your child to use the 20-20-20 rule. Every 20 minutes take a 20 second break to look at least 20 feet away.</p>
    </div>
    <svg class="footer-art" width="236" height="150" viewBox="0 0 236 150" role="img" aria-label="Photo of a young girl in glasses giving a high five to her eye doctor">
      <defs>
        <linearGradient id="envPhoto" x1="0" y1="0" x2="1" y2="1">
          <stop offset="0" stop-color="#e9edf0"/><stop offset=".55" stop-color="#c8d3de"/><stop offset="1" stop-color="#7a8ea8"/>
        </linearGradient>
        <clipPath id="envA"><rect x="0" y="0" width="88" height="150"/></clipPath>
        <clipPath id="envB"><rect x="88" y="0" width="70" height="150"/></clipPath>
        <clipPath id="envC"><rect x="158" y="0" width="78" height="150"/></clipPath>
      </defs>
      <path d="M0 42 Q110 -8 236 30 L236 150 L0 150 Z" fill="url(#envPhoto)"/>
      <path d="M0 40 Q110 -10 236 28" fill="none" stroke="var(--green)" stroke-width="8" clip-path="url(#envA)"/>
      <path d="M0 40 Q110 -10 236 28" fill="none" stroke="var(--yellow)" stroke-width="8" clip-path="url(#envB)"/>
      <path d="M0 40 Q110 -10 236 28" fill="none" stroke="var(--orange)" stroke-width="8" clip-path="url(#envC)"/>
    </svg>
  </article>

  <article class="panel panel--contact">
    <h2 class="heading">CONTACT US</h2>
    <div class="photo map" role="img" aria-label="Street map showing the clinic location"></div>
    <div class="photo exam-a" role="img" aria-label="Photo of a boy at an eye examination instrument"></div>
    <div class="photo exam-b" role="img" aria-label="Photo of an eye doctor fitting glasses on a smiling boy"></div>
    <h3 class="practice-name">Brookhollow Kids Vision</h3>
    <p class="address">2180 Linden Parkway, Harbor Point, VA 23499</p>
    <ul class="contact-list">
      <li><svg viewBox="0 0 24 24"><path d="M6.6 10.8a15.1 15.1 0 0 0 6.6 6.6l2.2-2.2c.3-.3.7-.4 1-.2 1.1.4 2.3.6 3.6.6.6 0 1 .4 1 1V20c0 .6-.4 1-1 1A17 17 0 0 1 3 4c0-.6.4-1 1-1h3.5c.6 0 1 .4 1 1 0 1.3.2 2.5.6 3.6.1.3 0 .7-.2 1z"/></svg>Voice: <strong>(555) 310-4420</strong></li>
      <li><svg viewBox="0 0 24 24"><path d="M12 3C6.5 3 2 6.8 2 11.5c0 2.3 1.1 4.4 2.9 6L4 22l4.6-2.3c1.1.3 2.2.5 3.4.5 5.5 0 10-3.8 10-8.6S17.5 3 12 3zM7.5 13a1.5 1.5 0 1 1 0-3 1.5 1.5 0 0 1 0 3zm4.5 0a1.5 1.5 0 1 1 0-3 1.5 1.5 0 0 1 0 3zm4.5 0a1.5 1.5 0 1 1 0-3 1.5 1.5 0 0 1 0 3z"/></svg>Text: <strong>(555) 310-4487</strong></li>
      <li><svg viewBox="0 0 24 24"><path d="M7 3h10v5H7zM4 9h16a2 2 0 0 1 2 2v6h-4v4H6v-4H2v-6a2 2 0 0 1 2-2zm4 7v3h8v-3z"/></svg>Fax: <strong>(555) 310-4495</strong></li>
    </ul>
  </article>

  <article class="panel panel--cover">
    <div class="brand">
      <span class="brand-dot"></span>
      <span class="brand-name">Brookhollow Kids Vision</span>
    </div>
    <h1 class="heading">MYOPIA CONTROL</h1>
    <div class="copy">
      <p>Myopia or nearsightedness causes blurry distance vision. Myopia is caused by the elongation of the eye, and progresses throughout childhood. Myopia is becoming increasingly common. More severe myopia and a higher glasses prescription is associated with a higher risk of eye problems involving the retina in adulthood, such as retinal problems and macular degeneration.</p>
      <p>Myopia control is meant to slow the growth of the eye, keeping the glasses prescription as low as possible and reducing the risk of ocular disease in adulthood. There are several treatment options</p>
    </div>
    <div class="photo" style="left:0;bottom:0;width:236px;height:168px;background:linear-gradient(180deg,var(--tint-blue) 0%,#dfe4ec 25%,#c9cfd8 60%,#8b7f76 100%);" role="img" aria-label="Photo of a boy having his eyes measured by a smiling optometrist"></div>
  </article>
</section>

<section class="sheet sheet--inside">

  <article class="panel panel--lenses">
    <h2 class="heading">LUMORA CORVANE<br>GLASSES LENSES</h2>
    <div class="photo media-box media-box--glasses" role="img" aria-label="Photo of hands holding a pair of black-framed glasses"></div>
    <div class="copy">
      <p>FDA market authorized Lumora Corvane glasses lenses have been shown to slow myopia progression by about 50% in children aged 6-12.</p>
      <p>These lenses are a great treatment option because all your child needs to do is wear glasses. They look almost identical to ordinary glasses, but use specialized optics to signal the brain to slow the growth of myopic eyes.</p>
    </div>
    <svg class="footer-art" width="236" height="150" viewBox="0 0 236 150" role="img" aria-label="Photo of a smiling girl adjusting her round glasses in front of an eye chart">
      <defs>
        <linearGradient id="lensPhoto" x1="0" y1="0" x2="1" y2="1">
          <stop offset="0" stop-color="#e6d6c9"/><stop offset=".5" stop-color="#f1e2dc"/><stop offset="1" stop-color="#d9dde3"/>
        </linearGradient>
        <clipPath id="lA"><rect x="0" y="0" width="88" height="150"/></clipPath>
        <clipPath id="lB"><rect x="88" y="0" width="70" height="150"/></clipPath>
        <clipPath id="lC"><rect x="158" y="0" width="78" height="150"/></clipPath>
      </defs>
      <path d="M0 40 Q110 -6 236 32 L236 150 L0 150 Z" fill="url(#lensPhoto)"/>
      <path d="M0 38 Q110 -8 236 30" fill="none" stroke="var(--green-light)" stroke-width="8" clip-path="url(#lA)"/>
      <path d="M0 38 Q110 -8 236 30" fill="none" stroke="var(--yellow-light)" stroke-width="8" clip-path="url(#lB)"/>
      <path d="M0 38 Q110 -8 236 30" fill="none" stroke="var(--orange)" stroke-width="8" clip-path="url(#lC)"/>
    </svg>
  </article>

  <article class="panel panel--drops">
    <h2 class="heading">LOW-DOSE<br>ATROPINE</h2>
    <div class="photo media-box media-box--drops" role="img" aria-label="Photo of a small eye drop bottle"></div>
    <div class="copy">
      <p>These eyedrops have been studied for over 20 years and have been shown to slow myopia progression by about 50% when used consistently.</p>
      <p>Low-dose atropine is simple to add to your daily routine. One drop is placed in each eye before bed each evening. These are ordered from a compounding pharmacy and mailed directly to your home.</p>
    </div>
    <svg class="footer-art" width="236" height="150" viewBox="0 0 236 150" role="img" aria-label="Photo of a curly-haired boy wearing a trial frame for an eye test">
      <defs>
        <linearGradient id="dropPhoto" x1="0" y1="0" x2="1" y2="1">
          <stop offset="0" stop-color="#ebe7e2"/><stop offset=".5" stop-color="#c9a487"/><stop offset="1" stop-color="#3d4a66"/>
        </linearGradient>
        <clipPath id="dA"><rect x="0" y="0" width="88" height="150"/></clipPath>
        <clipPath id="dB"><rect x="88" y="0" width="70" height="150"/></clipPath>
        <clipPath id="dC"><rect x="158" y="0" width="78" height="150"/></clipPath>
      </defs>
      <path d="M0 40 Q110 -6 236 32 L236 150 L0 150 Z" fill="url(#dropPhoto)"/>
      <path d="M0 38 Q110 -8 236 30" fill="none" stroke="var(--green-light)" stroke-width="8" clip-path="url(#dA)"/>
      <path d="M0 38 Q110 -8 236 30" fill="none" stroke="var(--yellow-light)" stroke-width="8" clip-path="url(#dB)"/>
      <path d="M0 38 Q110 -8 236 30" fill="none" stroke="var(--orange)" stroke-width="8" clip-path="url(#dC)"/>
    </svg>
  </article>

  <article class="panel panel--contacts">
    <h2 class="heading">LOW-DOSE<br>ATROPINE</h2>
    <div class="photo media-box media-box--lens" role="img" aria-label="Photo of two soft contact lenses"></div>
    <div class="copy">
      <p>FDA-approved ClearPath lenses have been shown to slow myopia progression by about 50% in children aged 8-12.</p>
      <p>Contact lenses can be a great fit for many children, especially active children or those who do not enjoy wearing glasses. Many children as young as 7 or 8 are successful at wearing contacts.</p>
    </div>
    <svg class="footer-art" width="236" height="150" viewBox="0 0 236 150" role="img" aria-label="Close-up photo of a contact lens being placed on an eye">
      <defs>
        <linearGradient id="contactPhoto" x1="0" y1="0" x2="1" y2="1">
          <stop offset="0" stop-color="#c9a995"/><stop offset=".45" stop-color="#8f7a70"/><stop offset="1" stop-color="#1d1a1a"/>
        </linearGradient>
        <clipPath id="cA"><rect x="0" y="0" width="88" height="150"/></clipPath>
        <clipPath id="cB"><rect x="88" y="0" width="70" height="150"/></clipPath>
        <clipPath id="cC"><rect x="158" y="0" width="78" height="150"/></clipPath>
      </defs>
      <path d="M0 40 Q110 -6 236 32 L236 150 L0 150 Z" fill="url(#contactPhoto)"/>
      <path d="M0 38 Q110 -8 236 30" fill="none" stroke="var(--green-light)" stroke-width="8" clip-path="url(#cA)"/>
      <path d="M0 38 Q110 -8 236 30" fill="none" stroke="var(--yellow-light)" stroke-width="8" clip-path="url(#cB)"/>
      <path d="M0 38 Q110 -8 236 30" fill="none" stroke="#f29a55" stroke-width="8" clip-path="url(#cC)"/>
    </svg>
  </article>
</section>

</body>
</html>
```